Bao Lotus Menu Design Project

This project is pretty straight forward. You will be given 3 files which include the following:
1. Our proposed menu
2. Our Company logo
3. A sample menu on what we are looking for design wise

Your job is to create a visually pleasing menu that is simple, clean and fresh. Please refer to our home website for additional information. (www.baolotus-example.com) Must be in eps or equivalent format.

Target Market(s)

20s to 40s

Industry/Entity Type

It Company

Requirements
Must have
• Company log
Must be in EPS format

```html
<!DOCTYPE html>
<html lang="en">
<head>
<meta charset="utf-8">
<title>Bao Lotus Menu</title>
<link href="https://fonts.googleapis.com/css2?family=Righteous&family=PT+Sans+Narrow:wght@400;700&display=swap" rel="stylesheet">
<style>
:root{
  --backdrop:#dde4ec;
  --paper:#ffffff;
  --ink:#3a3a3a;
  --muted:#6b6b6b;
  --silver-1:#f4f4f4;
  --silver-2:#c9c9c9;
  --silver-3:#9a9a9a;
  --brand-red:#d3262b;
  --orange:#ee8a23;
  --amber:#f2a81d;
  --green:#8db53a;
  --red:#c9302c;
  --wine:#a3242c;
  --brown:#a5662b;
}
*{box-sizing:border-box;margin:0;padding:0}
html,body{width:878px;height:1200px;overflow:hidden}
body{background:var(--backdrop);font-family:"PT Sans Narrow",Arial,sans-serif;color:var(--ink);padding:12px;display:flex;flex-direction:column;gap:12px}
.spread{display:flex;height:582px;box-shadow:0 2px 8px rgba(0,0,0,.18)}
.page{position:relative;width:427px;height:100%;background:var(--paper);overflow:hidden;display:flex;flex-direction:column}
.page + .page{border-left:1px solid #e2e2e2}
.page-head{position:relative;height:64px;flex:none}
.page-head svg{position:absolute;inset:0;width:100%;height:100%}
.brand{position:absolute;top:10px;left:50%;transform:translateX(-50%);display:flex;align-items:center;gap:4px;font-family:"Righteous",sans-serif;font-size:15px;color:var(--brand-red);white-space:nowrap}
.brand-mark{width:8px;height:8px;background:var(--brand-red)}
.page-foot{height:34px;flex:none;margin:auto 30px 8px;background:linear-gradient(90deg,transparent,var(--silver-2) 30%,var(--silver-3) 50%,var(--silver-2) 70%,transparent);border-radius:50%;opacity:.55}
.page-body{padding:2px 22px 0;flex:1;display:flex;flex-direction:column;gap:6px}
.cols{display:grid;grid-template-columns:1fr 1fr;gap:0 16px}
.section-title{font-family:"Righteous",sans-serif;font-size:12px;text-align:center;letter-spacing:.5px;margin:4px 0 3px}
.offer{font-weight:700;font-size:7px;text-align:center;line-height:1.25;margin-bottom:4px}
.dish{margin-bottom:4px}
.dish-line{display:flex;justify-content:space-between;gap:6px}
.dish-name{font-family:"Righteous",sans-serif;font-size:7px;text-transform:uppercase;letter-spacing:.2px}
.price{font-size:7px;font-weight:700;white-space:nowrap;text-align:right}
.dish-desc{font-size:6.4px;line-height:1.2;color:var(--muted)}
.seafood .section-title,.seafood .dish-name{color:var(--orange)}
.veg .section-title,.veg .dish-name{color:var(--green)}
.gf .section-title,.gf .dish-name{color:var(--red)}
.rice .section-title,.rice .dish-name,.noodles .section-title,.noodles .dish-name{color:var(--orange)}
.drinks .section-title,.drinks .dish-name{color:var(--wine)}
.tea .section-title,.tea .dish-name{color:var(--brown)}
.dimsum .section-title,.dimsum .dish-name{color:var(--amber)}
.starters .section-title,.starters .dish-name{color:var(--orange)}
.soup .section-title,.soup .dish-name{color:var(--orange)}
.salad .section-title,.salad .dish-name{color:var(--green)}
.chicken .section-title,.chicken .dish-name{color:var(--red)}
.meat .section-title,.meat .dish-name{color:var(--wine)}
</style>
</head>
<body>

<section class="spread">
  <article class="page">
    <header class="page-head">
      <svg viewBox="0 0 427 64" preserveAspectRatio="none" role="img" aria-label="Silver damask ornament band">
        <defs><linearGradient id="band1" x1="0" y1="0" x2="0" y2="1"><stop offset="0" stop-color="#e9e9e9"/><stop offset="1" stop-color="#c4c4c4"/></linearGradient></defs>
        <path d="M0 0H427V34Q213 74 0 34Z" fill="url(#band1)"/>
      </svg>
      <div class="brand"><span class="brand-mark"></span>Bao Lotus</div>
    </header>
    <div class="page-body">
      <div class="seafood">
        <h2 class="section-title">SEAFOOD</h2>
        <p class="offer">Enjoy a Half Chinese Chicken Salad or Plain Fried Rice with any entrée for $5.50<br>Can replace Seafood with Tofu for $1.50</p>
        <div class="cols">
          <div>
            <div class="dish"><div class="dish-line"><span class="dish-name">Crispy Spicy Honey Shrimp</span><span class="price">13.95</span></div><p class="dish-desc">Crispy large shrimp with red bell peppers, scallions, and chili peppers in a sweet honey sauce.</p></div>
            <div class="dish"><div class="dish-line"><span class="dish-name">Kung Pao Triple Treasures</span><span class="price">13.95</span></div><p class="dish-desc">Large shrimp, beef, and chicken breast with scallions, peanuts, water chestnuts, and chili peppers.</p></div>
            <div class="dish"><div class="dish-line"><span class="dish-name">Honey Walnut Shrimp</span><span class="price">13.95</span></div><p class="dish-desc">Lightly crisped savory shrimp with honey-glazed walnuts.</p></div>
            <div class="dish"><div class="dish-line"><span class="dish-name">Fish with Ginger Soy Sauce</span><span class="price">15.95</span></div><p class="dish-desc">Whole white fish fillet steamed with ginger and topped with green onions and cilantro.</p></div>
            <div class="dish"><div class="dish-line"><span class="dish-name">Shrimp with Snow Peas</span><span class="price">13.95</span></div><p class="dish-desc">Large shrimp with snow peas, water chestnuts, carrots, and ginger in a white wine sauce.</p></div>
          </div>
          <div>
            <div class="dish"><div class="dish-line"><span class="dish-name">Shrimp with Lobster Sauce</span><span class="price">13.95</span></div><p class="dish-desc">Large shrimp, eggs, ground pork, snow peas, water chestnuts, and red bell peppers sautéed in a lobster sauce.</p></div>
            <div class="dish"><div class="dish-line"><span class="dish-name">Salt and Pepper Shrimp</span><span class="price">13.95</span></div><p class="dish-desc">Lightly battered large shrimp with a pepper spice, served with bell peppers and white crunchies.</p></div>
            <div class="dish"><div class="dish-line"><span class="dish-name">Cashew Shrimp</span><span class="price">13.95</span></div><p class="dish-desc">Large shrimp with zucchini, onions, and roasted cashews in oyster sauce.</p></div>
            <div class="dish"><div class="dish-line"><span class="dish-name">Orange Shrimp</span><span class="price">13.95</span></div><p class="dish-desc">Large crispy shrimp with onions and red and green bell peppers in a sweet orange sauce.</p></div>
          </div>
        </div>
      </div>
      <div class="cols">
        <div class="veg">
          <h2 class="section-title">VEGETABLES</h2>
          <p class="offer">Enjoy a Half Chinese Chicken Salad or Plain Fried Rice with any entrée for $5.50<br>Can add Tofu for $1.50</p>
          <div class="dish"><div class="dish-line"><span class="dish-name">Fragrant Vegetables</span><span class="price">8.95</span></div><p class="dish-desc">Mixed vegetables with white wine, curry, garlic, black bean, kung pao, or vegetarian sauce.</p></div>
          <div class="dish"><div class="dish-line"><span class="dish-name">Vegetable Lettuce Wraps</span><span class="price">9.95</span></div><p class="dish-desc">Black mushrooms, bell peppers, water chestnuts, smoked tofu, pine nuts, and white crunchies.</p></div>
          <div class="dish"><div class="dish-line"><span class="dish-name">Szechwan String Beans</span><span class="price">8.95</span></div><p class="dish-desc">Blue lake green beans and garlic sautéed with pickled szechwan vegetables.</p></div>
          <div class="dish"><div class="dish-line"><span class="dish-name">Tofu with Black Mushrooms</span><span class="price">7.95</span></div><p class="dish-desc">Fried tofu triangles sautéed with scallions, black mushrooms, water chestnuts, and cabbage.</p></div>
          <div class="dish"><div class="dish-line"><span class="dish-name">Bok Choy with Black Mushrooms</span><span class="price">6.95</span></div><p class="dish-desc">Baby bok choy and black mushrooms sautéed in a brown sauce.</p></div>
          <div class="dish"><div class="dish-line"><span class="dish-name">Spicy Garlic Eggplant</span><span class="price">8.95</span></div><p class="dish-desc">Sautéed chinese eggplant, red onions, and scallions in a spicy garlic sauce.</p></div>
          <div class="dish"><div class="dish-line"><span class="dish-name">Salt and Pepper Tofu</span><span class="price">7.95</span></div><p class="dish-desc">Lightly battered soft tofu cubes with a pepper spice, bell peppers and white crunchies.</p></div>
        </div>
        <div class="gf">
          <h2 class="section-title">GLUTEN FREE</h2>
          <div class="dish"><div class="dish-line"><span class="dish-name">Steamed Ginger Fish</span><span class="price">7.77</span></div><p class="dish-desc">Whole fish steamed with ginger and scallions.</p></div>
          <div class="dish"><div class="dish-line"><span class="dish-name">Garlic Green Beans</span><span class="price">7.77</span></div><p class="dish-desc">Tossed with fresh garlic and sea salt.</p></div>
          <div class="dish"><div class="dish-line"><span class="dish-name">Plain Steamed Chicken</span><span class="price">7.77</span></div><p class="dish-desc">White meat chicken with steamed mixed vegetables.</p></div>
          <div class="dish"><div class="dish-line"><span class="dish-name">Lemon Shrimp Bowl</span><span class="price">7.77</span></div><p class="dish-desc">Shrimp, bok choy and rice with lemon.</p></div>
          <div class="dish"><div class="dish-line"><span class="dish-name">Sesame Tofu Plate</span><span class="price">7.77</span></div><p class="dish-desc">Tofu with broccoli, carrots and sesame oil.</p></div>
          <div class="dish"><div class="dish-line"><span class="dish-name">Ginger Beef Rice</span><span class="price">7.77</span></div><p class="dish-desc">Flank steak with ginger over steamed rice.</p></div>
        </div>
      </div>
    </div>
    <div class="page-foot" role="img" aria-label="Silver scroll flourish"></div>
  </article>

  <article class="page">
    <header class="page-head">
      <svg viewBox="0 0 427 64" preserveAspectRatio="none" role="img" aria-label="Silver damask ornament band">
        <defs><linearGradient id="band2" x1="0" y1="0" x2="0" y2="1"><stop offset="0" stop-color="#e9e9e9"/><stop offset="1" stop-color="#c4c4c4"/></linearGradient></defs>
        <path d="M0 0H427V34Q213 74 0 34Z" fill="url(#band2)"/>
      </svg>
      <div class="brand"><span class="brand-mark"></span>Bao Lotus</div>
    </header>
    <div class="page-body cols">
      <div>
        <div class="rice">
          <h2 class="section-title">MUSHU &amp; RICE</h2>
          <div class="dish"><div class="dish-line"><span class="dish-name">Crab and Asparagus Fried Rice</span><span class="price">13.95</span></div><p class="dish-desc">White fried rice with dungeness crab, asparagus, and egg white topped with fried onions. No soy sauce.</p></div>
          <div class="dish"><div class="dish-line"><span class="dish-name">Yang Chow Rice</span><span class="price">9.25</span></div><p class="dish-desc">White fried rice with shrimp, barbecue pork, peas, carrots, and eggs. No soy sauce.</p></div>
          <div class="dish"><div class="dish-line"><span class="dish-name">Mushu</span><span class="price">7.85</span></div><p class="dish-desc">Chicken, pork, or vegetable mushu with sautéed vegetables, mushrooms, and eggs. Wrapped in two thin pancakes.</p></div>
          <div class="dish"><div class="dish-line"><span class="dish-name">Fried Rice</span><span class="price">7.85</span></div><p class="dish-desc">Chicken, pork, or vegetable with eggs, scallions, and fried rice sauce. For beef or shrimp add $1.00.</p></div>
          <div class="dish"><div class="dish-line"><span class="dish-name">Steamed Rice</span><span class="price">Small 1.25<br>Large 1.75</span></div><p class="dish-desc">Choice of White or Brown.</p></div>
        </div>
        <div class="noodles">
          <h2 class="section-title">NOODLES</h2>
          <div class="dish"><div class="dish-line"><span class="dish-name">Lo Mein</span><span class="price">10.85</span></div><p class="dish-desc">Soft lo mein noodles with shredded vegetables and chicken, pork, or vegetables. Beef or shrimp add $1.00.</p></div>
          <div class="dish"><div class="dish-line"><span class="dish-name">Chow Mein</span><span class="price">12.85</span></div><p class="dish-desc">Crispy egg noodles or soft lo mein noodles with large vegetables and chicken, pork, or vegetables.</p></div>
          <div class="dish"><div class="dish-line"><span class="dish-name">Pad Thai</span><span class="price">12.85</span></div><p class="dish-desc">Rice noodles with chicken, shrimp, eggs, onions, and scallions topped with peanuts and cilantro.</p></div>
          <div class="dish"><div class="dish-line"><span class="dish-name">Peanut Noodles</span><span class="price">8.85</span></div><p class="dish-desc">Soft lo mein noodles with scallions, chopped peanuts, preserved szechwan vegetables, and a spicy peanut sauce.</p></div>
          <div class="dish"><div class="dish-line"><span class="dish-name">Singapore Noodles</span><span class="price">9.95</span></div><p class="dish-desc">Shrimp, barbecue pork, bean sprouts, onions, egg, and bell peppers with rice noodles in a curry sauce.</p></div>
          <div class="dish"><div class="dish-line"><span class="dish-name">Chow Fun</span><span class="price">10.95</span></div><p class="dish-desc">Chicken, pork, or vegetables with bean sprouts, scallions and wide rice noodles.</p></div>
        </div>
      </div>
      <div>
        <div class="drinks">
          <h2 class="section-title">BEVERAGES</h2>
          <div class="dish"><div class="dish-line"><span class="dish-name">Fjord Spring (Sparkling or Still)</span><span class="price">4.00<br>6.50</span></div><p class="dish-desc">Small (375ml) / Large (800ml)</p></div>
          <div class="dish"><div class="dish-line"><span class="dish-name">Soda</span><span class="price">2.75</span></div><p class="dish-desc">Cola, Diet Cola, Lemon-Lime, Cherry Cola, Orange Soda</p></div>
          <div class="dish"><div class="dish-line"><span class="dish-name">Lemonade</span><span class="price"></span></div></div>
          <div class="dish"><div class="dish-line"><span class="dish-name">Orange &amp; Cranberry Juice</span><span class="price">3.50</span></div></div>
          <div class="dish"><div class="dish-line"><span class="dish-name">Black Kettle French Press Coffee</span><span class="price">3.95</span></div><p class="dish-desc">Caffeinated or Decaffeinated</p></div>
          <div class="dish"><div class="dish-line"><span class="dish-name">Iced Teas</span><span class="price">2.75</span></div><p class="dish-desc">Traditional, Mango, Blackberry Jasmine Green.</p></div>
        </div>
        <div class="tea">
          <h2 class="section-title">LANTERN TEA BY THE POT</h2>
          <div class="dish"><div class="dish-line"><span class="dish-name">Green Kukicha Tea</span><span class="price">3.75</span></div><p class="dish-desc">Often enjoyed for its health benefits, this tea has a fresh green, grassy taste with a crisp finish.</p></div>
          <div class="dish"><div class="dish-line"><span class="dish-name">Ginger Chamomile Tea</span><span class="price">3.75</span></div><p class="dish-desc">This unique chamomile blend is velvety, yet mellow with a complex finish of cinnamon, apple, and lime.</p></div>
          <div class="dish"><div class="dish-line"><span class="dish-name">White Coconut Crème</span><span class="price">3.75</span></div><p class="dish-desc">Tender white peony leaves blended with cornflower, safflower, and sweet creamy coconut.</p></div>
          <div class="dish"><div class="dish-line"><span class="dish-name">Wuyi Oolong Tea</span><span class="price">3.75</span></div><p class="dish-desc">Long beautiful leaves unwind and unfurl when steeped to release a smooth, rice flavor with earthy tones.</p></div>
          <div class="dish"><div class="dish-line"><span class="dish-name">Premium Kaleido Tea</span><span class="price">4.25</span></div><p class="dish-desc">Hand-tied white tea blossoms into a rainbow of jasmine and amaranth flowers.</p></div>
          <div class="dish"><div class="dish-line"><span class="dish-name">Jasmine Reserve Tea</span><span class="price">3.75</span></div><p class="dish-desc">Organic fair trade green tea repeatedly baked and scented with fresh jasmine blossoms.</p></div>
          <div class="dish"><div class="dish-line"><span class="dish-name">English Breakfast Tea</span><span class="price">3.75</span></div><p class="dish-desc">A smooth malty brew with a clean finish, this is our house's traditional blend.</p></div>
          <div class="dish"><div class="dish-line"><span class="dish-name">Chamomile Clementine Tea</span><span class="price">3.75</span></div><p class="dish-desc">This unique chamomile blend is velvety, yet mellow with a complex finish. Caffeine-Free.</p></div>
        </div>
      </div>
    </div>
    <div class="page-foot" role="img" aria-label="Silver scroll flourish"></div>
  </article>
</section>

<section class="spread">
  <article class="page">
    <header class="page-head">
      <svg viewBox="0 0 427 64" preserveAspectRatio="none" role="img" aria-label="Silver damask ornament band">
        <defs><linearGradient id="band3" x1="0" y1="0" x2="0" y2="1"><stop offset="0" stop-color="#e9e9e9"/><stop offset="1" stop-color="#c4c4c4"/></linearGradient></defs>
        <path d="M0 0H427V34Q213 74 0 34Z" fill="url(#band3)"/>
      </svg>
      <div class="brand"><span class="brand-mark"></span>Bao Lotus</div>
    </header>
    <div class="page-body">
      <div class="dimsum">
        <h2 class="section-title">DIM SUM</h2>
        <div class="cols">
          <div>
            <div class="dish"><div class="dish-line"><span class="dish-name">Pan Fried Potstickers</span><span class="price">8.50</span></div><p class="dish-desc">Pan-fried potstickers with chicken or pork. Served with apricot dipping sauce.</p></div>
            <div class="dish"><div class="dish-line"><span class="dish-name">Steamed Dumplings</span><span class="price">8.25</span></div><p class="dish-desc">Five steamed dumplings with chicken or vegetables.</p></div>
            <div class="dish"><div class="dish-line"><span class="dish-name">Szechwan Dumplings</span><span class="price">8.25</span></div><p class="dish-desc">Five chicken dumplings tossed in a spicy szechwan sauce.</p></div>
            <div class="dish"><div class="dish-line"><span class="dish-name">Spring Rolls</span><span class="price">7.25</span></div><p class="dish-desc">Two chicken or vegetable spring rolls with apricot sauce.</p></div>
            <div class="dish"><div class="dish-line"><span class="dish-name">Wonton Chips</span><span class="price">6.95</span></div><p class="dish-desc">Two crispy wonton skins filled with real crab and sweetened cream cheese.</p></div>
          </div>
          <div>
            <div class="dish"><div class="dish-line"><span class="dish-name">Bao</span><span class="price">5.85</span></div><p class="dish-desc">Three fluffy steamed chinese buns filled with barbecue pork.</p></div>
            <div class="dish"><div class="dish-line"><span class="dish-name">Shrimp Toast</span><span class="price">5.85</span></div><p class="dish-desc">Four pieces of fried toast with shrimp, onions, bamboo shoots, and water chestnuts.</p></div>
            <div class="dish"><div class="dish-line"><span class="dish-name">Shu Mai</span><span class="price">5.85</span></div><p class="dish-desc">Six steamed open-face dumplings with pork, shrimp, and mushrooms.</p></div>
            <div class="dish"><div class="dish-line"><span class="dish-name">Cold Bamboo Chicken</span><span class="price">8.95</span></div><p class="dish-desc">Six chicken breast tenders marinated in soy sauce, sesame oil, and cilantro.</p></div>
            <div class="dish"><div class="dish-line"><span class="dish-name">Assorted Appetizers</span><span class="price">9.85</span></div><p class="dish-desc">Two chicken potstickers, two fried chicken wontons, two pot wrapped chicken, and one spring roll.</p></div>
          </div>
        </div>
      </div>
      <div class="cols">
        <div class="starters">
          <h2 class="section-title">STARTERS</h2>
          <div class="dish"><div class="dish-line"><span class="dish-name">Edamame</span><span class="price">4.00</span></div><p class="dish-desc">Steamed Soybean Pods.</p></div>
          <div class="dish"><div class="dish-line"><span class="dish-name">Lightly Battered Calamari Strips</span><span class="price">5.85</span></div><p class="dish-desc">Six calamari strips, lightly battered with a garlic ginger aioli.</p></div>
          <div class="dish"><div class="dish-line"><span class="dish-name">Lotus House Cake</span><span class="price">14.95<br>18.95</span></div><p class="dish-desc">Jumbo lump maryland crab meat seasoned with our house sauce. Lunch / Dinner.</p></div>
          <div class="dish"><div class="dish-line"><span class="dish-name">Dim Sum and Then Some</span><span class="price"></span></div><p class="dish-desc">Choose three or four items: potstickers, steamed dumplings, szechwan dumplings, spring roll, shrimp toast, chicken salad, hot &amp; sour soup, wonton soup, or mushu.</p></div>
        </div>
        <div class="soup">
          <h2 class="section-title">SOUP</h2>
          <div class="dish"><div class="dish-line"><span class="dish-name">Wonton Soup</span><span class="price">4.95<br>7.50</span></div><p class="dish-desc">Chicken or pork wonton dumplings with spinach and scallions in chicken broth.</p></div>
          <div class="dish"><div class="dish-line"><span class="dish-name">Miso Soup</span><span class="price">4.95<br>7.50</span></div><p class="dish-desc">Miso based soup with tofu and scallions.</p></div>
          <div class="dish"><div class="dish-line"><span class="dish-name">Hot and Sour Soup</span><span class="price">7.25</span></div><p class="dish-desc">Shredded pork, carrots, egg, and soft tofu.</p></div>
          <div class="dish"><div class="dish-line"><span class="dish-name">Velvet Corn Soup</span><span class="price">7.25</span></div><p class="dish-desc">Cellophane noodles, chicken, sweet corn, green peas, and egg. No modifications.</p></div>
        </div>
      </div>
      <div class="salad">
        <h2 class="section-title">SALAD</h2>
        <p class="offer">Can replace Chicken with Tofu for $1.50</p>
        <div class="cols">
          <div class="dish"><div class="dish-line"><span class="dish-name">Chinese Chicken Salad</span><span class="price">10.50</span></div><p class="dish-desc">Shredded lettuce, chicken breast, scallions, carrots, toasted almonds, and white crunchies with tart red ginger dressing.</p></div>
          <div class="dish"><div class="dish-line"><span class="dish-name">Sesame Chicken Salad</span><span class="price">9.85</span></div><p class="dish-desc">Shredded lettuce, chicken breast, red cabbage, carrots, fresh oranges, scallions, and sesame dressing.</p></div>
        </div>
      </div>
    </div>
    <div class="page-foot" role="img" aria-label="Silver scroll flourish"></div>
  </article>

  <article class="page">
    <header class="page-head">
      <svg viewBox="0 0 427 64" preserveAspectRatio="none" role="img" aria-label="Silver damask ornament band">
        <defs><linearGradient id="band4" x1="0" y1="0" x2="0" y2="1"><stop offset="0" stop-color="#e9e9e9"/><stop offset="1" stop-color="#c4c4c4"/></linearGradient></defs>
        <path d="M0 0H427V34Q213 74 0 34Z" fill="url(#band4)"/>
      </svg>
      <div class="brand"><span class="brand-mark"></span>Bao Lotus</div>
    </header>
    <div class="page-body">
      <div class="chicken">
        <h2 class="section-title">CHICKEN</h2>
        <p class="offer">For white meat chicken, add $1.00<br>Enjoy a Half Chinese Chicken Salad or Plain Fried Rice with any entrée for $5.50<br>Can replace Chicken with Tofu for $1.50</p>
        <div class="cols">
          <div>
            <div class="dish"><div class="dish-line"><span class="dish-name">Orange Chicken</span><span class="price">11.85</span></div><p class="dish-desc">Crispy chicken with onions and red and green bell peppers in a tangy orange sauce.</p></div>
            <div class="dish"><div class="dish-line"><span class="dish-name">General Tso's Chicken</span><span class="price">11.85</span></div><p class="dish-desc">Crispy dark meat chicken with chili peppers in a spicy tangerine sauce.</p></div>
            <div class="dish"><div class="dish-line"><span class="dish-name">Kung Pao Chicken</span><span class="price">11.75</span></div><p class="dish-desc">Dark meat chicken with red bell peppers, peanuts, water chestnuts in spicy red sauce.</p></div>
            <div class="dish"><div class="dish-line"><span class="dish-name">Chicken Lettuce Wraps</span><span class="price">11.85</span></div><p class="dish-desc">Minced white meat chicken, red bell peppers, water chestnuts, and pine nuts. Served with four lettuce cups.</p></div>
            <div class="dish"><div class="dish-line"><span class="dish-name">Chicken with Asparagus</span><span class="price">11.85</span></div><p class="dish-desc">Chicken breast with asparagus and carrots in a lemon white wine sauce.</p></div>
            <div class="dish"><div class="dish-line"><span class="dish-name">Chicken with Snow Peas</span><span class="price">11.85</span></div><p class="dish-desc">Chicken breast sautéed with snow peas, fresh mushrooms, carrots, and sliced garlic.</p></div>
          </div>
          <div>
            <div class="dish"><div class="dish-line"><span class="dish-name">Mandarin Chicken</span><span class="price">11.75</span></div><p class="dish-desc">Crispy chicken breast topped with scallions in a tangerine sauce.</p></div>
            <div class="dish"><div class="dish-line"><span class="dish-name">Szechwan Chicken</span><span class="price">11.75</span></div><p class="dish-desc">Dark meat chicken with bamboo shoots, celery, water chestnuts, and toasted almonds.</p></div>
            <div class="dish"><div class="dish-line"><span class="dish-name">Lemon Chicken</span><span class="price">11.75</span></div><p class="dish-desc">Crispy chicken breast with a tart lemon sauce on the side.</p></div>
            <div class="dish"><div class="dish-line"><span class="dish-name">Cashew Chicken</span><span class="price">11.85</span></div><p class="dish-desc">Chicken breast, zucchini, onions, garlic, ginger, and cashews tossed in oyster sauce.</p></div>
            <div class="dish"><div class="dish-line"><span class="dish-name">Curry Chicken</span><span class="price">11.85</span></div><p class="dish-desc">Chicken breast with potatoes, onions, green peas and carrots in a curry sauce.</p></div>
            <div class="dish"><div class="dish-line"><span class="dish-name">Sweet and Sour Chicken</span><span class="price">11.75</span></div><p class="dish-desc">Crispy chicken breast, bell peppers, onions, and pineapple in a sweet and sour sauce.</p></div>
          </div>
        </div>
      </div>
      <div class="meat">
        <h2 class="section-title">BEEF &amp; PORK</h2>
        <p class="offer">Rice is not included. Add rice $1.25<br>Enjoy a Half Chinese Chicken Salad or Plain Fried Rice with any entrée for $5.50<br>Can replace Beef/Pork with Tofu for $1.50</p>
        <div class="cols">
          <div>
            <div class="dish"><div class="dish-line"><span class="dish-name">Mongolian Beef</span><span class="price">12.85</span></div><p class="dish-desc">Flank steak, garlic, ginger, and green onions on a bed of white crunchies.</p></div>
            <div class="dish"><div class="dish-line"><span class="dish-name">Beef and Broccoli</span><span class="price">12.25</span></div><p class="dish-desc">Flank steak, broccoli, and black mushrooms sautéed in a garlic brown sauce.</p></div>
            <div class="dish"><div class="dish-line"><span class="dish-name">Pepper Steak</span><span class="price">12.25</span></div><p class="dish-desc">Flank steak, peppers, onions, and garlic in black pepper sauce.</p></div>
            <div class="dish"><div class="dish-line"><span class="dish-name">Sliced Barbecued Pork</span><span class="price">11.85</span></div><p class="dish-desc">Tender slices of juicy pork topped with scallions in a barbecue sauce.</p></div>
          </div>
          <div>
            <div class="dish"><div class="dish-line"><span class="dish-name">Barbecued Spareribs</span><span class="price">12.25</span></div><p class="dish-desc">Slow-roasted juicy pork ribs with barbecue sauce.</p></div>
            <div class="dish"><div class="dish-line"><span class="dish-name">Mandarin Beef</span><span class="price">12.85</span></div><p class="dish-desc">Crispy flank steak tossed with scallions in a tangerine sauce.</p></div>
            <div class="dish"><div class="dish-line"><span class="dish-name">Spicy Garlic Tender Beef</span><span class="price">12.85</span></div><p class="dish-desc">Flank steak, tomato, water chestnuts, zucchini, onions, and spicy garlic sauce.</p></div>
            <div class="dish"><div class="dish-line"><span class="dish-name">Ma Po Tofu</span><span class="price">7.85</span></div><p class="dish-desc">Soft tofu cubes with ground pork or chicken cooked in szechwan-style sauce.</p></div>
          </div>
        </div>
      </div>
    </div>
    <div class="page-foot" role="img" aria-label="Silver scroll flourish"></div>
  </article>
</section>

</body>
</html>
```